Marvane Painting Epoxy Flyer

We need a promotional flyer for a new epoxy floor coatings division of our painting company. We do epoxy garage floor coatings and paver sealing. It needs to be based on and very similar to the attached flyer. The garage floor picture needs to look more realistic, and the before and after pavers pictures should look less shiny but still a good contrast. Include attached logo

```html
<!DOCTYPE html>
<html lang="en">
<head>
<meta charset="utf-8">
<title>Marvane Painting – Garage &amp; Driveway Flyer</title>
<link rel="stylesheet" href="https://fonts.googleapis.com/css2?family=Oswald:wght@400;500;600&family=Roboto:wght@700;900&family=Playfair+Display:ital,wght@1,700&display=swap">
<style>
  :root {
    --navy: #0b2a6b;
    --blue: #0a3f95;
    --green: #3e8e0b;
    --ink: #111111;
    --paper: #ffffff;
    --stage: #f2f2f2;
    --blue-tint: #e8effb;
    --green-tint: #eef8e4;
    --line: #9fb3d9;
  }
  * { box-sizing: border-box; margin: 0; padding: 0; }
  html, body { width: 970px; height: 1200px; overflow: hidden; background: var(--stage); }
  .flyer {
    position: absolute; left: 21px; top: 0; width: 928px; height: 1200px;
    background: linear-gradient(180deg, #f6f6f7 0%, #ffffff 22%, #ffffff 100%);
    font-family: "Oswald", sans-serif; color: var(--ink);
  }
  .abs { position: absolute; }

  .brand { left: 60px; top: 110px; display: flex; align-items: center; gap: 12px; }
  .brand-dot { width: 34px; height: 34px; border-radius: 50%; background: var(--blue); }
  .brand-name { font-family: "Roboto", sans-serif; font-weight: 700; font-size: 22px; color: #222; letter-spacing: .5px; }

  .headline { left: 389px; top: 28px; line-height: 1; font-weight: 600; }
  .headline .l1 { font-size: 62px; display: block; color: var(--ink); }
  .headline .l2 { font-size: 62px; display: block; margin-top: 4px; }
  .headline .blue { color: var(--blue); }
  .headline .green { color: var(--green); }
  .tagline { left: 394px; top: 177px; width: 376px; height: 36px; }
  .tagline span {
    position: absolute; left: 14px; top: 2px; font-family: "Playfair Display", serif; font-style: italic;
    font-weight: 700; font-size: 25px; color: #fff; white-space: nowrap;
  }

  .photo-label { font-family: "Roboto", sans-serif; font-weight: 900; font-size: 23px; color: #fff; }

  .card { left: 45px; width: 353px; border-radius: 6px; }
  .card-head { height: 36px; border-radius: 6px 6px 4px 4px; color: #fff; font-weight: 500; font-size: 22px; text-align: center; line-height: 36px; }
  .card ul { list-style: none; padding: 10px 0 0 0; }
  .card li { display: flex; align-items: center; gap: 6px; font-size: 15.5px; font-weight: 400; color: #222; height: 24px; }
  .card li svg { width: 18px; height: 18px; flex: none; }
  .card.epoxy { top: 706px; height: 160px; background: var(--blue-tint); }
  .card.epoxy .card-head { background: var(--blue); }
  .card.epoxy ul { padding-left: 52px; }
  .card.paver { top: 882px; height: 160px; background: var(--green-tint); }
  .card.paver .card-head { background: var(--green); }
  .card.paver ul { padding-left: 41px; }

  .promise { left: 412px; top: 706px; width: 482px; height: 336px; background: var(--blue); border-radius: 6px; overflow: hidden; }
  .promise-side { position: absolute; left: 0; top: 0; width: 90px; height: 100%; background: var(--navy); }
  .promise-side p {
    position: absolute; left: 45px; top: 168px; transform: translate(-50%,-50%) rotate(-90deg);
    width: 320px; color: #fff; font-weight: 500; font-size: 21px; line-height: 1.12; text-align: center;
  }
  .promise-notch { position: absolute; left: 90px; top: 156px; width: 0; height: 0; border-top: 12px solid transparent; border-bottom: 12px solid transparent; border-left: 12px solid var(--navy); }
  .feature { position: absolute; left: 126px; display: flex; align-items: center; gap: 14px; }
  .feature-icon { width: 76px; height: 76px; border-radius: 50%; background: #fff; display: flex; align-items: center; justify-content: center; box-shadow: 0 3px 6px rgba(0,0,0,.25); }
  .feature-icon svg { width: 46px; height: 46px; }
  .feature p { color: #fff; font-size: 19px; line-height: 1.3; font-weight: 400; }
  .divider { position: absolute; left: 216px; width: 244px; border-top: 1.5px dashed var(--line); }

  .cta { left: 47px; top: 1064px; width: 850px; height: 84px; border: 1.5px solid var(--green); border-radius: 10px; background: #f5f5f5; overflow: hidden; }
  .cta-tab { position: absolute; left: 0; top: 0; height: 100%; width: 260px; }
  .cta-tab p { position: absolute; left: 30px; top: 6px; color: #fff; font-weight: 500; font-size: 33px; line-height: 1.02; }
  .cta-phone { position: absolute; left: 276px; top: 18px; display: flex; align-items: center; gap: 8px; }
  .cta-phone span { font-family: "Roboto", sans-serif; font-weight: 900; font-size: 45px; color: var(--ink); letter-spacing: .5px; }
  .cta-note { position: absolute; left: 676px; top: 18px; font-style: italic; color: var(--green); font-size: 17px; line-height: 1.05; font-weight: 400; }
</style>
</head>
<body>
<main class="flyer">

  <div class="abs brand">
    <div class="brand-dot"></div>
    <span class="brand-name">MARVANE PAINTING</span>
  </div>

  <h1 class="abs headline">
    <span class="l1">Upgarde Your</span>
    <span class="l2"><span class="blue">Garage &amp;</span> <span class="green">Driveway</span></span>
  </h1>
  <div class="abs tagline">
    <svg width="376" height="36" viewBox="0 0 376 36"><polygon points="0,0 376,0 360,36 0,36" fill="#0b2a6b"/></svg>
    <span>From worn-out to like new</span>
  </div>

  <!-- Garage before / after -->
  <svg class="abs" style="left:45px;top:249px" width="555" height="434" viewBox="0 0 555 434">
    <defs>
      <linearGradient id="garage-old" x1="0" y1="0" x2="0" y2="1">
        <stop offset="0" stop-color="#e4e1da"/><stop offset=".2" stop-color="#9a9384"/><stop offset="1" stop-color="#6d685d"/>
      </linearGradient>
      <linearGradient id="garage-new" x1="0" y1="0" x2="0" y2="1">
        <stop offset="0" stop-color="#e8e2d8"/><stop offset=".2" stop-color="#8d9298"/><stop offset="1" stop-color="#6b7178"/>
      </linearGradient>
    </defs>
    <g role="img" aria-label="Photo of a stained, worn concrete garage floor before coating">
      <polygon points="0,0 348,0 258,434 0,434" fill="url(#garage-old)"/>
    </g>
    <g role="img" aria-label="Photo of the same garage with a grey flake epoxy floor after coating">
      <polygon points="352,0 555,0 555,434 262,434" fill="url(#garage-new)"/>
    </g>
    <line x1="350" y1="0" x2="260" y2="434" stroke="#fff" stroke-width="4"/>
    <polygon points="186,213 302,213 293,253 177,253" fill="#0a3f95"/>
    <polygon points="302,213 426,213 417,253 293,253" fill="#3e8e0b"/>
    <text class="photo-label" x="184" y="242" fill="#fff" font-family="Roboto, sans-serif" font-weight="900" font-size="23">BEFORE</text>
    <text class="photo-label" x="315" y="242" fill="#fff" font-family="Roboto, sans-serif" font-weight="900" font-size="23">AFTER</text>
  </svg>

  <!-- Pavers before / after -->
  <svg class="abs" style="left:607px;top:249px" width="286" height="434" viewBox="0 0 286 434">
    <defs>
      <linearGradient id="pavers-old" x1="0" y1="0" x2="0" y2="1">
        <stop offset="0" stop-color="#6a5a48"/><stop offset=".25" stop-color="#7a6c5e"/><stop offset="1" stop-color="#857566"/>
      </linearGradient>
      <linearGradient id="pavers-new" x1="0" y1="0" x2="0" y2="1">
        <stop offset="0" stop-color="#5e4a36"/><stop offset=".25" stop-color="#8c6547"/><stop offset="1" stop-color="#a7714a"/>
      </linearGradient>
    </defs>
    <rect role="img" aria-label="Photo of faded brick paver patio beside a wooden fence before sealing" x="0" y="0" width="286" height="217" fill="url(#pavers-old)"/>
    <rect role="img" aria-label="Photo of the same paver patio with restored warm colour after sealing" x="0" y="223" width="286" height="211" fill="url(#pavers-new)"/>
    <polygon points="0,179 125,179 118,217 0,217" fill="#0a3f95"/>
    <text x="14" y="207" fill="#fff" font-family="Roboto, sans-serif" font-weight="900" font-size="23">BEFORE</text>
    <polygon points="122,394 286,394 286,434 115,434" fill="#3e8e0b"/>
    <text x="194" y="424" fill="#fff" font-family="Roboto, sans-serif" font-weight="900" font-size="23">AFTER</text>
  </svg>

  <section class="abs card epoxy">
    <h2 class="card-head">EPROXY FLOOR COATINGS</h2>
    <ul>
      <li><svg viewBox="0 0 20 20"><circle cx="10" cy="10" r="8" fill="none" stroke="#0b2a6b" stroke-width="2"/><path d="M6 10l3 3 7-8" fill="none" stroke="#0b2a6b" stroke-width="2.2"/></svg>Durable, long-lasting finish</li>
      <li><svg viewBox="0 0 20 20"><circle cx="10" cy="10" r="8" fill="none" stroke="#0b2a6b" stroke-width="2"/><path d="M6 10l3 3 7-8" fill="none" stroke="#0b2a6b" stroke-width="2.2"/></svg>Slip-resistant texture</li>
      <li><svg viewBox="0 0 20 20"><circle cx="10" cy="10" r="8" fill="none" stroke="#0b2a6b" stroke-width="2"/><path d="M6 10l3 3 7-8" fill="none" stroke="#0b2a6b" stroke-width="2.2"/></svg>Covers cracks &amp; imperfections</li>
      <li><svg viewBox="0 0 20 20"><circle cx="10" cy="10" r="8" fill="none" stroke="#0b2a6b" stroke-width="2"/><path d="M6 10l3 3 7-8" fill="none" stroke="#0b2a6b" stroke-width="2.2"/></svg>Easy to clean &amp; maintain</li>
    </ul>
  </section>

  <section class="abs card paver">
    <h2 class="card-head">PAVER SEALING</h2>
    <ul>
      <li><svg viewBox="0 0 20 20"><circle cx="10" cy="10" r="8" fill="none" stroke="#0b2a6b" stroke-width="2"/><path d="M6 10l3 3 7-8" fill="none" stroke="#3e8e0b" stroke-width="2.2"/></svg>Restores color &amp; enhances appearance</li>
      <li><svg viewBox="0 0 20 20"><circle cx="10" cy="10" r="8" fill="none" stroke="#0b2a6b" stroke-width="2"/><path d="M6 10l3 3 7-8" fill="none" stroke="#3e8e0b" stroke-width="2.2"/></svg>Protects from sun fading</li>
      <li><svg viewBox="0 0 20 20"><circle cx="10" cy="10" r="8" fill="none" stroke="#0b2a6b" stroke-width="2"/><path d="M6 10l3 3 7-8" fill="none" stroke="#3e8e0b" stroke-width="2.2"/></svg>Helps prevent weeds &amp; sand loss</li>
      <li><svg viewBox="0 0 20 20"><circle cx="10" cy="10" r="8" fill="none" stroke="#0b2a6b" stroke-width="2"/><path d="M6 10l3 3 7-8" fill="none" stroke="#3e8e0b" stroke-width="2.2"/></svg>Easier to clean &amp; maintain</li>
    </ul>
  </section>

  <section class="abs promise">
    <div class="promise-side"><p>Practical upgardes that protect and improve your home</p></div>
    <div class="promise-notch"></div>

    <div class="feature" style="top:27px">
      <div class="feature-icon"><svg viewBox="0 0 48 48"><path d="M24 5l15 6v11c0 10-7 17-15 21C16 39 9 32 9 22V11z" fill="none" stroke="#0a3f95" stroke-width="3"/><path d="M17 24l6 6 10-12" fill="none" stroke="#3e8e0b" stroke-width="3.5"/></svg></div>
      <p>Licensed &amp;<br>Insured</p>
    </div>
    <div class="divider" style="top:116px"></div>

    <div class="feature" style="top:127px">
      <div class="feature-icon"><svg viewBox="0 0 48 48"><path d="M10 10l26 26" stroke="#3e8e0b" stroke-width="4" stroke-linecap="round"/><path d="M38 8l-26 26" stroke="#0a3f95" stroke-width="4" stroke-linecap="round"/><circle cx="11" cy="37" r="5" fill="none" stroke="#0a3f95" stroke-width="3"/><circle cx="37" cy="11" r="5" fill="none" stroke="#0a3f95" stroke-width="3"/></svg></div>
      <p>Family-Owned Local<br>Business</p>
    </div>
    <div class="divider" style="top:218px"></div>

    <div class="feature" style="top:224px">
      <div class="feature-icon"><svg viewBox="0 0 48 48"><path d="M24 32c-6-8-10-12-10-18a10 10 0 0120 0c0 6-4 10-10 18z" fill="none" stroke="#3e8e0b" stroke-width="3"/><circle cx="24" cy="14" r="4" fill="none" stroke="#3e8e0b" stroke-width="3"/><path d="M8 40l5-8h22l5 8z" fill="none" stroke="#0a3f95" stroke-width="3"/></svg></div>
      <p>Serving Prescott &amp;<br>Surrounding Areas</p>
    </div>
  </section>

  <section class="abs cta">
    <svg class="cta-tab" viewBox="0 0 260 84" width="260" height="84"><polygon points="0,0 230,0 252,42 230,84 0,84" fill="#3e8e0b"/><polygon points="0,0 224,0 246,42 224,84 0,84" fill="#0a3f95"/></svg>
    <div class="cta-tab"><p>CALL FOR A<br>FREE EXTIMATE</p></div>
    <div class="cta-phone">
      <svg width="40" height="40" viewBox="0 0 40 40"><path d="M10 5l6 7-4 4c2 5 6 9 11 11l4-4 7 6-4 6C19 35 5 21 4 9z" fill="none" stroke="#3e8e0b" stroke-width="2.6" stroke-linejoin="round"/><path d="M24 6a11 11 0 0110 10M24 12a5 5 0 014 4" fill="none" stroke="#3e8e0b" stroke-width="2.4" stroke-linecap="round"/></svg>
      <span>928-555-0174</span>
    </div>
    <p class="cta-note">Fast, professional<br>service you can trust</p>
  </section>

</main>
</body>
</html>
```